Welcome Postcard for existing church in new facility

I need a postcard to express the 4 strong points of our ministry. I have attached a sample postcard that we really liked as a start point. Our four strengths are;

LOVE
WORSHIP
DIVERSITY
DOCTRINE

I want to make sure the colors used are vivid and provide plenty of pop.

I have provide images to coincide with the four ministry strengths and they are named according the the strength the coincide with, pick whichever you think is best graphically.

our twitter handle is @BHDAWNOK
our FB handle is /BHDAWNOK
our Youtube handle is /BrightHarbor

I must have all PSD layers in case last minutes changes need to be made. THIS IS A REQUIREMENT.

Target Market(s)

General Population

Industry/Entity Type

Non-Profit

Font styles to use
Sans Serif

Requirements
Must have
• I must have all PSD layers in case last minutes changes need to be made. THIS IS A REQUIREMENT.
Nice to have
• Be attractive and market friendly is US marketplace
Should not have
• Please do not submit multiple designs with slight deviations. If you submit multiple designs please make them totally different one from another. We will not consider your design if you spam us.

```html
<!DOCTYPE html>
<html lang="en">
<head>
<meta charset="utf-8">
<title>Bright Harbor Ministries – Welcome Postcard</title>
<link rel="stylesheet" href="https://fonts.googleapis.com/css2?family=Questrial&family=Source+Sans+3:wght@400;500;600;700&display=swap">
<style>
  :root {
    --ink: #0b0b0c;
    --white: #ffffff;
    --love-a: #ee4e9f;
    --love-b: #c64a8c;
    --worship-a: #7d6330;
    --worship-b: #f2782a;
    --diversity-a: #13984a;
    --diversity-b: #b9c734;
    --doctrine-a: #6b6461;
    --doctrine-b: #1174c2;
    --site: #3aa3dc;
  }
  * { margin: 0; padding: 0; box-sizing: border-box; }
  html, body { width: 782px; height: 1200px; overflow: hidden; background: var(--ink); }
  .postcard {
    position: relative; width: 782px; height: 1200px; overflow: hidden;
    background: var(--ink); color: var(--white);
    font-family: "Source Sans 3", sans-serif;
  }

  /* Header */
  .masthead { position: absolute; left: 0; top: 0; width: 100%; height: 170px; text-align: center; }
  .brand { position: absolute; top: 46px; left: 0; width: 100%; display: flex; justify-content: center; align-items: center; gap: 22px; }
  .brand-mark { font-family: "Questrial", sans-serif; font-size: 58px; letter-spacing: -2px; line-height: 1; }
  .brand-name { font-family: "Questrial", sans-serif; font-size: 39px; line-height: 1; }
  .masthead-rule { position: absolute; top: 112px; left: 90px; width: 600px; height: 1px;
    background: linear-gradient(90deg, transparent, #d8d8d8 15%, #d8d8d8 85%, transparent); }
  .address { position: absolute; top: 126px; left: 0; width: 100%; font-family: "Questrial", sans-serif; font-size: 22px; color: #e8e8e8; }

  /* Bands */
  .band { position: absolute; left: 0; top: 0; width: 782px; height: 1200px; }
  .band-fill { position: absolute; inset: 0; }
  .photo { position: absolute; top: 0; bottom: 0; }
  .band-love { clip-path: polygon(0 206px, 782px 162px, 782px 430px, 0 376px); }
  .band-love .band-fill { background: linear-gradient(90deg, var(--love-a), var(--love-b)); }
  .band-love .photo { left: 330px; right: 0; background: linear-gradient(90deg, rgba(214,90,150,0), rgba(190,110,140,.75) 40%, rgba(150,70,110,.8)); }

  .band-worship { clip-path: polygon(0 386px, 782px 438px, 782px 623px, 0 679px); }
  .band-worship .band-fill { background: linear-gradient(90deg, var(--worship-a), #b08a40 45%, #e8a23a 70%, var(--worship-b)); }
  .band-worship .photo { left: 0; right: 180px; background: linear-gradient(90deg, rgba(70,50,25,.7), rgba(140,110,60,.4) 60%, rgba(200,140,50,0)); }

  .band-diversity { clip-path: polygon(0 685px, 782px 633px, 782px 895px, 0 853px); }
  .band-diversity .band-fill { background: linear-gradient(90deg, var(--diversity-a), #3aa845 40%, #8cb63a 70%, var(--diversity-b)); }
  .band-diversity .photo { left: 360px; right: 0; background: linear-gradient(90deg, rgba(120,150,50,0), rgba(110,120,40,.55) 40%, rgba(150,160,70,.5)); }

  .band-doctrine { clip-path: polygon(0 862px, 782px 905px, 782px 1086px, 0 1086px); }
  .band-doctrine .band-fill { background: linear-gradient(90deg, var(--doctrine-a), #8d8478 35%, #3f7fb0 65%, var(--doctrine-b)); }
  .band-doctrine .photo { left: 0; right: 200px; background: linear-gradient(90deg, rgba(90,70,60,.55), rgba(190,180,165,.45) 45%, rgba(60,110,170,0)); }

  /* Band content */
  .pillar { position: absolute; display: flex; align-items: center; }
  .pillar-word { font-weight: 500; font-size: 77px; line-height: 1; letter-spacing: -1px; text-shadow: 0 1px 4px rgba(0,0,0,.25); }
  .pillar-note { position: absolute; font-size: 17px; line-height: 22px; font-weight: 500; text-shadow: 0 1px 3px rgba(0,0,0,.4); }
  .pillar-icon { display: block; fill: none; stroke: var(--white); stroke-width: 3.5; stroke-linejoin: round; }

  .love-icon { position: absolute; left: 46px; top: 262px; }
  .love-word { position: absolute; left: 126px; top: 254px; }
  .love-note { left: 338px; top: 286px; }

  .worship-word { position: absolute; right: 130px; top: 489px; }
  .worship-icon { position: absolute; left: 672px; top: 486px; }
  .worship-note { right: 490px; top: 514px; text-align: right; }

  .diversity-icon { position: absolute; left: 46px; top: 730px; }
  .diversity-word { position: absolute; left: 110px; top: 724px; font-size: 80px; }
  .diversity-note { left: 496px; top: 742px; }

  .doctrine-word { position: absolute; left: 256px; top: 962px; }
  .doctrine-icon { position: absolute; left: 652px; top: 976px; }
  .doctrine-note { right: 551px; top: 982px; text-align: right; }

  /* Footer */
  .footer { position: absolute; left: 0; top: 1086px; width: 100%; height: 114px; }
  .social { position: absolute; top: 20px; display: flex; align-items: center; gap: 8px;
    font-size: 13px; font-weight: 700; letter-spacing: .2px; }
  .social-dot { width: 18px; height: 18px; border-radius: 3px; background: var(--site); }
  .social-facebook { left: 60px; }
  .social-twitter { left: 338px; }
  .social-video { left: 604px; }
  .site { position: absolute; top: 54px; left: 0; width: 100%; text-align: center;
    font-family: "Questrial", sans-serif; font-size: 22px; letter-spacing: 6px; color: var(--site); }
</style>
</head>
<body>
<main class="postcard">

  <header class="masthead">
    <div class="brand">
      <span class="brand-mark">BH</span>
      <span class="brand-name">Bright Harbor Ministries</span>
    </div>
    <div class="masthead-rule"></div>
    <p class="address">2210 West Cedar Ave, Lawton, OK 73505</p>
  </header>

  <section class="band band-love">
    <div class="band-fill"></div>
    <div class="photo" role="img" aria-label="Photo of two women sharing a joyful hug"></div>
  </section>
  <section class="band band-worship">
    <div class="band-fill"></div>
    <div class="photo" role="img" aria-label="Photo of a keyboard player and a singer leading worship in a church hall"></div>
  </section>
  <section class="band band-diversity">
    <div class="band-fill"></div>
    <div class="photo" role="img" aria-label="Photo of a congregation with raised hands in worship"></div>
  </section>
  <section class="band band-doctrine">
    <div class="band-fill"></div>
    <div class="photo" role="img" aria-label="Photo of an open Bible held in a lap"></div>
  </section>

  <!-- Love -->
  <svg class="pillar-icon love-icon" width="72" height="66" viewBox="0 0 72 66" aria-hidden="true">
    <path d="M36 62 C14 44 3 32 3 19 C3 9 11 3 19 3 C27 3 33 8 36 14 C39 8 45 3 53 3 C61 3 69 9 69 19 C69 32 58 44 36 62 Z"/>
  </svg>
  <h2 class="pillar-word love-word">LOVE</h2>
  <p class="pillar-note love-note">Not simply a feeling, but<br>a decision and a commitment.</p>

  <!-- Worship -->
  <p class="pillar-note worship-note">The natural reaction to the<br>very presence of the Lord.</p>
  <h2 class="pillar-word worship-word">WORSHIP</h2>
  <svg class="pillar-icon worship-icon" width="52" height="72" viewBox="0 0 52 72" aria-hidden="true">
    <path d="M19 2 H33 V20 H50 V34 H33 V70 H19 V34 H2 V20 H19 Z"/>
  </svg>

  <!-- Diversity -->
  <svg class="pillar-icon diversity-icon" width="58" height="58" viewBox="0 0 58 58" aria-hidden="true">
    <circle cx="29" cy="29" r="26"/>
    <ellipse cx="29" cy="29" rx="11" ry="26"/>
    <line x1="29" y1="3" x2="29" y2="55"/>
    <line x1="3" y1="29" x2="55" y2="29"/>
    <path d="M7 16 H51 M7 42 H51"/>
  </svg>
  <h2 class="pillar-word diversity-word">DIVERSITY</h2>
  <p class="pillar-note diversity-note">Unique individuals,<br>making up one unified body.</p>

  <!-- Doctrine -->
  <p class="pillar-note doctrine-note">The expression of<br>a fundamental truth.</p>
  <h2 class="pillar-word doctrine-word">DOCTRINE</h2>
  <svg class="pillar-icon doctrine-icon" width="70" height="56" viewBox="0 0 70 56" aria-hidden="true">
    <path d="M35 10 L35 52 L3 44 L3 2 Z"/>
    <path d="M35 10 L67 2 L67 44 L35 52 Z"/>
  </svg>

  <footer class="footer">
    <div class="social social-facebook"><span class="social-dot"></span>/BHDAWNOK</div>
    <div class="social social-twitter"><span class="social-dot"></span>@BHDAWNOK</div>
    <div class="social social-video"><span class="social-dot"></span>/BrightHarbor</div>
    <p class="site">brightharbor.org</p>
  </footer>

</main>
</body>
</html>
```